Webdesign für vielseitiges Unternehmen
Zielgruppe
Die Seite wird HOCHMOOR-ART oder DESIGN heißen.
Das Unternehmen bietet folgende Segmente an:
1. Möbelstücke (meist Unikate, da restauriert mit eigener Kreation)
2. Fotografien
3. Malerei
4. Interieurdesign (Gestalten, Einrichten von Apartments, Häusern, Shops etc.) (hier muss natürlich mehr Platz für Informationstext sein.
5. Gallery. - Infos zu Öffnungszeiten und Bilder ebenfalls.
6. Die Location ist für Events buchbar
(7.) Blogg wenns nicht zu aufwändig ist. (hier möchte ich gern Bilder posten die ich irgendwo finde und als gut erachte. Oder Produkte. Wichtig ist, dass bei Verbreitung von Fremdpostings, immer die Quelle eingefügt werden muss. Am besten automatisch. Ich muss zu dem Post noch eigenes Kommentar abgeben können.
Für jedes Segment soll eine Unterseite geschaffen werden.
Die Produktfotos sollen clean aufgebaut sein. Am besten je Produkt 1 Bild pro Seite. Vielleicht erst nachdem man auf ein Bild in der Auswahl geklickt hat?? 3 nebeneinander und dann neue Zeile.
Unter den Bildern (hauptsächlich Querformat aber Hochformat muss auch gehen) müssen Angaben stehen:
-Art
-Size
-Auflage
-Preis
-liken für Social Media oder weiterleiten (wenn möglich)
-Fragen zu diesem Produkt ( wenn hier jemand klickt und etwas schreibt, muss ich eine mail erhalten, wo ich direkt ersehen kann, zu welchem Produkt die Frage zugeordnet ist.
Pro Artikel müssen mehrere Bilder eingestellt werden können, die der Client durch einfaches klicken durchklicken kann.
Die Seite soll clean, chic und Edel wirken. Hauptsächlich über Bilder. Shopsystem ist wegen Aufwandskosten erstmal nicht geplant)
Ich muss die Seite selber pflegen können, auch SEO Optimieren (ohne Programierkenntnisse)
Die Seite soll eine Seite für verschiedene Aspekte sein wie:
- Gallerie
hier wird die Gallerie vorgestellt und Bilder gezeigt von Ausstellungen und Künstlervorstellung..
Aufgabenstellung
Schwarz- Weiß
Akzente eventuell in Patinagrün oder Grünspan oder Malachitgrün oder Gold
Mobilgeräte responsiv

```html
<!DOCTYPE html>
<html lang="de">
<head>
<meta charset="utf-8">
<title>HOCHMOOR – Interieur · Design · Galerie</title>
<link href="https://fonts.googleapis.com/css2?family=Figtree:wght@300;400;500&family=Inter:wght@400&display=swap" rel="stylesheet">
<style>
  :root{
    --page:#f5f5f5;
    --card:#ffffff;
    --ink:#1f2a3a;
    --muted:#8a8f96;
    --green:#4a7463;
    --green-soft:#6d8b6c;
    --mint:#dde5e1;
    --line:#e3e3e3;
  }
  *{box-sizing:border-box;margin:0;padding:0}
  html,body{width:1200px;height:2526px;overflow:hidden}
  body{background:var(--page);font-family:"Figtree",sans-serif;color:var(--ink);position:relative}
  .abs{position:absolute}

  .brand{left:0;width:1200px;top:62px;text-align:center}
  .brand-name{font-size:54px;font-weight:400;letter-spacing:5px;line-height:56px;color:var(--ink)}
  .brand-tag{font-size:13px;letter-spacing:4.5px;margin-top:10px;color:var(--ink)}

  .card{left:99px;width:1002px;background:var(--card);border-radius:12px;overflow:hidden}

  .office-photo{position:absolute;left:28px;top:0;width:441px;height:100%;
    background:
      linear-gradient(90deg,rgba(255,255,255,0) 0%,rgba(255,255,255,0) 86%,#fff 100%),
      linear-gradient(0deg,rgba(40,36,34,.55) 0%,rgba(40,36,34,0) 18%),
      radial-gradient(ellipse 70px 90px at 170px 175px,#a33a3a 0%,rgba(163,58,58,.6) 45%,rgba(163,58,58,0) 100%),
      radial-gradient(ellipse 40px 48px at 150px 110px,#c79a7d 0%,rgba(199,154,125,0) 100%),
      radial-gradient(ellipse 90px 170px at 320px 340px,#7b5a3e 0%,rgba(123,90,62,.7) 45%,rgba(123,90,62,0) 100%),
      radial-gradient(ellipse 80px 120px at 345px 420px,#3d3f5a 0%,rgba(61,63,90,0) 100%),
      radial-gradient(ellipse 90px 150px at 80px 330px,#c9b28f 0%,rgba(201,178,143,.5) 50%,rgba(201,178,143,0) 100%),
      radial-gradient(ellipse 90px 110px at 130px 420px,#5a5c62 0%,rgba(90,92,98,0) 100%),
      radial-gradient(ellipse 70px 130px at 385px 130px,#8d6d55 0%,rgba(141,109,85,0) 100%),
      radial-gradient(ellipse 120px 60px at 230px 290px,#8e9196 0%,rgba(142,145,150,0) 100%),
      linear-gradient(180deg,#e9ebe8 0%,#d4d6d3 40%,#bfc0bd 70%,#a9a6a2 100%)}
  .card-body{position:absolute;left:529px;top:0;width:422px}
  .card-title{font-size:42px;font-weight:300;line-height:48px;color:var(--ink)}
  .card-text{font-size:13.4px;line-height:21.2px;color:var(--muted);font-weight:400}
  .card-text + .card-text{margin-top:21px}

  .about{top:201px;height:493px}
  .about .card-title{margin-top:64px}
  .about .card-text:first-of-type{margin-top:38px}

  .team{top:731px;height:386px;background:var(--green);color:#fff}
  .portrait-photo{position:absolute;left:469px;top:0;right:0;height:100%;
    background:
      linear-gradient(90deg,var(--green) 0%,rgba(74,116,99,0) 3%,rgba(74,116,99,0) 95%,var(--green) 100%),
      radial-gradient(ellipse 150px 170px at 320px 230px,#e3c6b6 0%,#d7b19d 45%,rgba(215,177,157,0) 100%),
      radial-gradient(ellipse 200px 120px at 300px 40px,#2a2426 0%,rgba(42,36,38,.8) 50%,rgba(42,36,38,0) 100%),
      radial-gradient(ellipse 110px 220px at 150px 230px,#3a2f2f 0%,rgba(58,47,47,.7) 50%,rgba(58,47,47,0) 100%),
      radial-gradient(ellipse 120px 160px at 470px 200px,#a7d4d6 0%,rgba(167,212,214,0) 100%),
      linear-gradient(90deg,#d9dddb 0%,#b7c4c2 20%,#c8b4a6 55%,#b8d6d4 85%,#8fc1c2 100%)}
  .team-body{position:absolute;left:85px;top:88px;width:305px}
  .team-name{font-size:31px;font-weight:300;line-height:38px}
  .team-role{font-size:16px;margin-top:4px}
  .team-quote{font-size:16px;line-height:21px;margin-top:20px}
  .btn{display:inline-block;border-radius:4px;font-size:17px;text-align:center}
  .btn-contact{margin-top:22px;width:140px;height:45px;line-height:45px;background:var(--green-soft);color:#fff}
  .slider-arrow{position:absolute;top:178px;width:16px;height:30px}
  .slider-arrow.prev{left:22px}
  .slider-arrow.next{right:22px}

  .jobs{top:1155px;height:493px}
  .jobs .card-title{margin-top:64px}
  .jobs .card-text{margin-top:38px}
  .btn-apply{margin-top:24px;width:140px;height:45px;line-height:45px;background:var(--mint);color:var(--ink)}

  .map{left:99px;top:1686px;width:1002px;height:408px;
    background:
      radial-gradient(ellipse 260px 120px at 180px 120px,#fafafa 0%,rgba(250,250,250,0) 100%),
      radial-gradient(ellipse 300px 140px at 720px 300px,#e4e4e4 0%,rgba(228,228,228,0) 100%),
      radial-gradient(ellipse 220px 160px at 500px 200px,#f8f8f8 0%,rgba(248,248,248,0) 100%),
      radial-gradient(ellipse 200px 110px at 880px 90px,#e7e7e7 0%,rgba(231,231,231,0) 100%),
      radial-gradient(ellipse 240px 130px at 260px 340px,#e9e9e9 0%,rgba(233,233,233,0) 100%),
      linear-gradient(160deg,#f2f2f2,#ebebeb)}
  .map-zoom{position:absolute;right:28px;top:28px;width:38px;height:84px;background:#fff;border-radius:3px}
  .map-share{position:absolute;right:28px;bottom:28px;width:42px;height:42px;background:#fff;border-radius:3px}
  .map-pin{position:absolute;left:480px;top:152px}

  .contact-bar{left:99px;top:2094px;width:1002px;height:63px;background:var(--card);border-radius:0 0 8px 8px;
    font-family:"Inter",sans-serif;font-size:14px;color:var(--ink)}
  .contact-item{position:absolute;top:0;height:63px;display:flex;align-items:center;gap:14px}

  .footer{left:0;top:2195px;width:1200px;height:246px;background:var(--card)}
  .footer-col{position:absolute;top:48px}
  .footer-title{font-size:20px;font-weight:400;color:var(--ink)}
  .footer-links{list-style:none;margin-top:24px;font-family:"Inter",sans-serif;font-size:14px;color:var(--muted)}
  .footer-links li{height:32px}
  .newsletter-text{font-family:"Inter",sans-serif;font-size:13.5px;line-height:16px;color:var(--muted);margin-top:20px;width:300px}
  .newsletter-form{display:flex;margin-top:30px;width:235px;height:38px;border:2px solid var(--green);border-radius:5px;overflow:hidden}
  .newsletter-input{flex:1;font-family:"Inter",sans-serif;font-size:12px;padding-left:12px;color:#b5b5b5;display:flex;align-items:center}
  .newsletter-send{width:60px;background:var(--green);display:flex;align-items:center;justify-content:center}

  .social{top:2470px;left:998px;display:flex;gap:28px}
  .social-dot{width:14px;height:14px;border-radius:50%;background:var(--ink)}
</style>
</head>
<body>

<header class="brand abs">
  <div class="brand-name">HOCHMOOR</div>
  <div class="brand-tag">INTERIEUR · DESIGN · GALERIE</div>
</header>

<section class="card about abs">
  <div class="office-photo" role="img" aria-label="Foto: Team im Gespräch in einem hellen Büro"></div>
  <div class="card-body">
    <h2 class="card-title">Über Uns</h2>
    <p class="card-text">Hier würde der Text hinkommen über Sie und Ihre Idee, was Sie bewegt und seit wann es die Firma gibt. und so weiter.</p>
    <p class="card-text">Lorem ipsum dolor sit amet, consetetur sadipscing elitr, sed diam nonumy eirmod tempor invidunt ut labore et dolore magna aliquyam erat, sed diam voluptua. At vero eos et accusam et justo duo dolores et ea rebum. Stet clita kasd gubergren, no sea takimata sanctus est Lorem ipsum dolor sit amet. Lorem ipsum dolor sit amet, consetetur sadipscing elitr, sed diam nonumy eirmod tempor invidunt ut labore et dolore magna aliquyam erat, sed diam voluptua. At vero eos et accusam et justo duo dolores et ea rebum. Stet clita kasd gubergren, no sea takimata sanctus est Lorem ipsum dolor sit amet.</p>
  </div>
</section>

<section class="card team abs">
  <div class="portrait-photo" role="img" aria-label="Porträtfoto der Geschäftsführerin"></div>
  <svg class="slider-arrow prev" viewBox="0 0 16 30"><path d="M14 1 1 15l13 14" fill="none" stroke="#fff" stroke-width="1.5"/></svg>
  <svg class="slider-arrow next" viewBox="0 0 16 30"><path d="M2 1l13 14L2 29" fill="none" stroke="#fff" stroke-width="1.5"/></svg>
  <div class="team-body">
    <h3 class="team-name">Selina<br>Marwald</h3>
    <p class="team-role">Geschäftsführerin</p>
    <p class="team-quote">“Irgendein Zitat der Geschäftsführung,<br>gern auch zweizeilig gedacht”</p>
    <span class="btn btn-contact">Kontaktieren</span>
  </div>
</section>

<section class="card jobs abs">
  <div class="office-photo" role="img" aria-label="Foto: Team im Gespräch in einem hellen Büro"></div>
  <div class="card-body">
    <h2 class="card-title">Jobs</h2>
    <p class="card-text">Lorem ipsum dolor sit amet, consetetur sadipscing elitr, sed diam nonumy eirmod tempor invidunt ut labore et dolore magna aliquyam erat, sed diam voluptua. At vero eos et accusam et justo duo dolores et ea rebum. Stet clita kasd gubergren, no sea takimata sanctus est Lorem ipsum dolor sit amet. Lorem ipsum dolor sit amet, consetetur sadipscing elitr, sed diam nonumy eirmod tempor invidunt ut labore et dolore magna aliquyam erat, sed diam voluptua. At vero eos et accusam et justo duo dolores et ea rebum. Stet clita kasd gubergren, no sea takimata sanctus est Lorem ipsum dolor sit amet.</p>
    <span class="btn btn-apply">Bewerben</span>
  </div>
</section>

<section class="map abs" role="img" aria-label="Karte mit dem Standort">
  <svg class="map-pin" width="40" height="52" viewBox="0 0 40 52"><path d="M20 1C9.5 1 1 9.3 1 19.6 1 33 20 51 20 51s19-18 19-31.4C39 9.3 30.5 1 20 1z" fill="var(--green)"/><circle cx="20" cy="19" r="6.5" fill="#fff"/></svg>
  <div class="map-zoom">
    <svg width="38" height="84" viewBox="0 0 38 84"><path d="M8 22h22M19 11v22M8 62h22" stroke="#555" stroke-width="1.5"/><path d="M4 42h30" stroke="var(--line)"/></svg>
  </div>
  <div class="map-share">
    <svg width="42" height="42" viewBox="0 0 42 42"><path d="M21 12v13M16 17l5-5 5 5M14 21v9h14v-9" fill="none" stroke="#444" stroke-width="1.4"/></svg>
  </div>
</section>

<div class="contact-bar abs">
  <div class="contact-item" style="left:168px">
    <svg width="20" height="20" viewBox="0 0 24 24"><path d="M5 3h4l2 5-2.5 1.5a11 11 0 0 0 6 6L16 13l5 2v4a2 2 0 0 1-2 2A17 17 0 0 1 3 5a2 2 0 0 1 2-2z" fill="none" stroke="var(--ink)" stroke-width="1.5"/></svg>
    <span>+00 987-654-32100</span>
  </div>
  <div class="contact-item" style="left:400px">
    <svg width="18" height="22" viewBox="0 0 18 22"><path d="M9 1a7 7 0 0 0-7 7c0 5 7 13 7 13s7-8 7-13a7 7 0 0 0-7-7z" fill="none" stroke="var(--ink)" stroke-width="1.5"/><circle cx="9" cy="8" r="2.5" fill="none" stroke="var(--ink)" stroke-width="1.5"/></svg>
    <span>12345 Musterstadt, Musterland</span>
  </div>
  <div class="contact-item" style="left:659px">
    <svg width="22" height="16" viewBox="0 0 22 16"><rect x="1" y="1" width="20" height="14" rx="1" fill="none" stroke="var(--ink)" stroke-width="1.5"/><path d="M1 2l10 7 10-7" fill="none" stroke="var(--ink)" stroke-width="1.5"/></svg>
    <span>info@hochmoor-art.com</span>
  </div>
</div>

<footer class="footer abs">
  <div class="footer-col" style="left:99px">
    <h4 class="footer-title">Links</h4>
    <ul class="footer-links"><li>Home</li><li>Shop</li><li>Blog</li><li>Contact</li></ul>
  </div>
  <div class="footer-col" style="left:355px">
    <h4 class="footer-title">Mehr infos</h4>
    <ul class="footer-links"><li>Über Uns</li><li>Team</li><li>Jobs</li><li>Impressum</li></ul>
  </div>
  <div class="footer-col" style="left:610px">
    <h4 class="footer-title">Support</h4>
    <ul class="footer-links"><li>FAQ</li><li>AGBs</li><li>Datenschutz</li></ul>
  </div>
  <div class="footer-col" style="left:866px">
    <h4 class="footer-title">Newsletter</h4>
    <p class="newsletter-text">Melden Sie sich jetzt für unseren Newsletter an und verpassen Sie keine Neuigkeiten.</p>
    <div class="newsletter-form">
      <div class="newsletter-input">Emailadresse</div>
      <div class="newsletter-send">
        <svg width="22" height="20" viewBox="0 0 22 20"><path d="M2 2l18 8-18 8 3-8z" fill="none" stroke="#fff" stroke-width="1.6" stroke-linejoin="round"/></svg>
      </div>
    </div>
  </div>
</footer>

<div class="social abs" aria-label="Soziale Netzwerke">
  <span class="social-dot" aria-label="Netzwerk 1"></span>
  <span class="social-dot" aria-label="Netzwerk 2"></span>
  <span class="social-dot" aria-label="Netzwerk 3"></span>
</div>

</body>
</html>
```